Kestrel Plumbing business card full re design & logo design

Kestrel Plumbing is a Sydney based mechanical plumbing contractor company.
We would like a full redesign with new logo etc which we can take to a future website, uniforms, vehicle sign writing etc.
Blue is my preferred choice of colour but i would be open to see a couple of alternatives thrown in the mix to see how they compare. I am open to see on white cards, black cards etc. Open to many new ideas.
Please see attached original business cards which have been used for the last 5 years.

Target Market(s)

Mechanical services industry.

Industry/Entity Type

Plumbing

Contact Information for Business Card

Dale Fenmore
Director

Mob: 0427 596 418
Email: dale@kestrelplumbing-demo.net.au
PO BOX 782
Larkfield NSW 2157
Lic: 518604k

Logo Text

Kestrel Plumbing

Font styles to use
Sans Serif

Colors
0655a3
3276b5
0792cd
33a6d7
85cae6
000000
333333
474747

Requirements
Must have
• Things that make it very professional and very well presented.
Nice to have
• Same description or very similar to attached uploaded file
Should not have
• Anything that makes it look unprofessional or cartoony.

```html
<!DOCTYPE html>
<html lang="en">
<head>
<meta charset="utf-8">
<title>Kestrel Plumbing – Business Card</title>
<link href="https://fonts.googleapis.com/css2?family=Arimo:wght@700&family=Hind:wght@400&display=swap" rel="stylesheet">
<style>
  :root {
    --page-bg: #c6c7c9;
    --card-navy: #013f69;
    --accent-red: #e31e2b;
    --text-white: #ffffff;
    --heading-font: "Arimo", Arial, sans-serif;
    --body-font: "Hind", Arial, sans-serif;
  }
  * { margin: 0; padding: 0; box-sizing: border-box; }
  html, body {
    width: 1200px; height: 1200px; overflow: hidden;
    background: var(--page-bg);
  }
  .canvas { position: relative; width: 1200px; height: 1200px; }
  .card {
    position: absolute; left: 288px; width: 682px; height: 380px;
    background: var(--card-navy); color: var(--text-white);
  }
  .card--front { top: 210px; }
  .card--back { top: 626px; }

  .brand-mark {
    position: absolute; left: 80px; top: 168px; width: 196px;
    display: flex; align-items: center; gap: 10px;
    font-family: var(--heading-font); font-weight: 700; font-size: 22px;
    line-height: 1; white-space: nowrap; color: var(--text-white);
  }
  .brand-mark__dot {
    width: 18px; height: 18px; border-radius: 50%;
    background: var(--text-white); flex: none;
  }

  .front-copy { position: absolute; left: 385px; top: 80px; }
  .company-name, .tagline {
    font-family: var(--heading-font); font-weight: 700;
    font-size: 27px; line-height: 31px; letter-spacing: -0.2px;
  }
  .company-name { color: var(--text-white); }
  .tagline { color: var(--accent-red); }
  .services { list-style: none; margin-top: 2px; }
  .services li {
    position: relative; padding-left: 12px;
    font-family: var(--body-font); font-size: 22px; line-height: 26px;
    letter-spacing: 0.3px;
  }
  .services li::before {
    content: ""; position: absolute; left: 0; top: 8px;
    width: 10px; height: 10px; border-radius: 50%;
    background: var(--accent-red);
  }

  .contact {
    position: absolute; right: 57px; top: 60px; text-align: right;
    font-family: var(--body-font); font-size: 22px; line-height: 27px;
    letter-spacing: 0.3px;
  }
  .contact__name {
    font-family: var(--heading-font); font-weight: 700;
    font-size: 26px; line-height: 30px; color: var(--accent-red);
  }
  .contact__lines { margin-top: 26px; }
  .contact__address { margin-top: 33px; padding-right: 7px; }
</style>
</head>
<body>
<main class="canvas">
  <section class="card card--front">
    <div class="brand-mark">
      <span class="brand-mark__dot"></span>
      <span class="brand-mark__name">Kestrel Plumbing</span>
    </div>
    <div class="front-copy">
      <h1 class="company-name">Kestrel Plumbing</h1>
      <p class="tagline">have the solution</p>
      <ul class="services">
        <li>make good</li>
        <li>refurbishment</li>
        <li>tenancy fit out</li>
        <li>plant room works</li>
        <li>shut downs</li>
        <li>change overs</li>
      </ul>
    </div>
  </section>

  <section class="card card--back">
    <div class="contact">
      <p class="contact__name">Dale Fenmore</p>
      <p class="contact__role">Director</p>
      <div class="contact__lines">
        <p>0427 596 418</p>
        <p>dale@kestrelplumbing-demo.net.au</p>
      </div>
      <div class="contact__address">
        <p>PO BOX 782</p>
        <p>Larkfield NSW 2157</p>
        <p>Lic: 518604k</p>
      </div>
    </div>
  </section>
</main>
</body>
</html>
```